Crestline Productions Business Logo and Card Design

PLEASE LIMIT your submission to maximum of 2 at a time.
Crestline Productions provides video production services, and produces videos, that help people connect in the spirit of unity and peace.Primarily I am looking for a logo that is simple to remember but the concept is fairly complex. The concept of the logo is a peace dove with an olive branch in it's mouth has it's wings around earth, symbolising that it is protecting earth with peace. If possible I'd like this logo done and delivered in high quality vector format, so I can use it for banners etc.Then the business card I just want a simple white card with the logo in the middle and contact info under the logo. Open to suggestions if you think there should be anything else included, but it must remain simple and uncluttered. Also incorporate something in the logo that says film and video e.g.: film strip or camera lens

Industry/Entity Type

Business

Contact Information for Business Card

Crestline Productions
www.crestline.example
darveen@crestline.example
+61 455 118 207

Requirements
Must have
• Logo must have the following:
• Peace Dove
• Olive branch
• Earth
• Something about video production (e.g.: film strip or camera lens or anything film related)

```html
<!DOCTYPE html>
<html lang="en">
<head>
<meta charset="utf-8">
<title>Crestline Productions – Business Card</title>
<link href="https://fonts.googleapis.com/css2?family=Open+Sans:wght@400;600&display=swap" rel="stylesheet">
<style>
  :root {
    --backdrop: #d9dadc;
    --card: #ffffff;
    --card-edge: #e2e2e2;
    --ink: #1c1c1c;
    --ink-soft: #3a3a3a;
    --rule: #cfcfcf;
    --icon-bg: #111111;
    --icon-fg: #ffffff;
  }
  * { box-sizing: border-box; margin: 0; padding: 0; }
  html, body {
    width: 1200px; height: 864px; overflow: hidden;
    background: var(--backdrop);
    font-family: "Open Sans", Arial, sans-serif;
    color: var(--ink);
  }
  .canvas { position: relative; width: 1200px; height: 864px; }

  .card {
    position: absolute;
    width: 580px; height: 330px;
    background: var(--card);
    border: 1px solid var(--card-edge);
    box-shadow: 0 6px 18px rgba(0,0,0,0.12);
  }
  .card--front { left: 190px; top: 70px; }
  .card--back  { left: 430px; top: 464px; }

  /* front */
  .front-mark {
    position: absolute; left: 0; right: 0; top: 112px;
    display: flex; flex-direction: column; align-items: center; gap: 14px;
  }
  .mark-dot {
    width: 46px; height: 46px; border-radius: 50%;
    background: var(--ink);
  }
  .front-name {
    font-size: 22px; font-weight: 600; letter-spacing: 3px;
    text-transform: uppercase; color: var(--ink);
  }

  /* back */
  .brand {
    position: absolute; right: 40px; top: 52px;
    display: flex; flex-direction: column; align-items: center; gap: 8px;
  }
  .brand-dot { width: 24px; height: 24px; border-radius: 50%; background: var(--ink); }
  .brand-name {
    font-size: 15px; font-weight: 600; letter-spacing: 2px;
    text-transform: uppercase; color: var(--ink-soft);
  }
  .holder { position: absolute; left: 40px; top: 118px; }
  .holder-name { font-size: 22px; font-weight: 600; color: var(--ink-soft); line-height: 1.1; }
  .holder-role { font-size: 13px; font-weight: 400; color: var(--ink); margin-top: 2px; }
  .divider {
    position: absolute; left: 190px; right: 40px; top: 166px;
    height: 1px; background: var(--rule);
  }
  .contacts {
    position: absolute; right: 40px; top: 196px;
    list-style: none; display: flex; flex-direction: column; gap: 4px;
  }
  .contact {
    display: flex; align-items: center; justify-content: flex-end; gap: 10px;
    font-size: 15px; line-height: 20px; color: var(--ink);
  }
  .contact-icon {
    width: 16px; height: 16px; flex: none; display: block;
  }
</style>
</head>
<body>
<main class="canvas">

  <section class="card card--front" aria-label="Card front">
    <div class="front-mark">
      <span class="mark-dot"></span>
      <span class="front-name">Crestline Productions</span>
    </div>
  </section>

  <section class="card card--back" aria-label="Card back">
    <div class="brand">
      <span class="brand-dot"></span>
      <span class="brand-name">Crestline Productions</span>
    </div>

    <div class="holder">
      <p class="holder-name">Elliot Marsh</p>
      <p class="holder-role">Managing Director</p>
    </div>
    <div class="divider"></div>

    <ul class="contacts">
      <li class="contact">+61 455 118 207
        <svg class="contact-icon" viewBox="0 0 16 16"><rect width="16" height="16" rx="3" fill="var(--icon-bg)"/><path d="M3.5 7 Q8 3 12.5 7 L11 8.5 L9.5 7.5 L6.5 7.5 L5 8.5 Z M5 9 H11 V12 H5 Z" fill="var(--icon-fg)"/></svg>
      </li>
      <li class="contact">+61 455 118 208
        <svg class="contact-icon" viewBox="0 0 16 16"><rect width="16" height="16" rx="3" fill="var(--icon-bg)"/><rect x="4" y="3" width="8" height="3" fill="var(--icon-fg)"/><rect x="3" y="7" width="10" height="6" rx="1" fill="var(--icon-fg)"/></svg>
      </li>
      <li class="contact">+61 455 118 209
        <svg class="contact-icon" viewBox="0 0 16 16"><rect width="16" height="16" rx="3" fill="var(--icon-bg)"/><rect x="5" y="2.5" width="6" height="11" rx="1" fill="var(--icon-fg)"/><rect x="6" y="4" width="4" height="7" fill="var(--icon-bg)"/></svg>
      </li>
      <li class="contact">darveen@crestline.example
        <svg class="contact-icon" viewBox="0 0 16 16"><rect width="16" height="16" rx="3" fill="var(--icon-bg)"/><rect x="3" y="4.5" width="10" height="7" fill="var(--icon-fg)"/><path d="M3 4.5 L8 8.5 L13 4.5" stroke="var(--icon-bg)" fill="none" stroke-width="1"/></svg>
      </li>
      <li class="contact">www.crestline.example
        <svg class="contact-icon" viewBox="0 0 16 16"><rect width="16" height="16" rx="3" fill="var(--icon-bg)"/><path d="M6.5 9.5 L9.5 6.5 M5.5 8 L4 9.5 A1.8 1.8 0 0 0 6.5 12 L8 10.5 M10.5 8 L12 6.5 A1.8 1.8 0 0 0 9.5 4 L8 5.5" stroke="var(--icon-fg)" fill="none" stroke-width="1.4" stroke-linecap="round"/></svg>
      </li>
    </ul>
  </section>

</main>
</body>
</html>
```